Web Page Re-designed

Looking to have this portion of a webpage on my site re-designed to look a little more clean and professional, the layout and organization of the data can be changed for example the location name does not have to keep repeating itself its schedule for a sports league

Reason: Still looking fo the right design

```html
<!DOCTYPE html>
<html lang="en">
<head>
<meta charset="utf-8">
<title>RPL Sports – Wednesday Co-Ed Ball Hockey Schedule</title>
<link href="https://fonts.googleapis.com/css2?family=Open+Sans:ital,wght@0,400;0,600;0,700;1,400;1,700;1,800&display=swap" rel="stylesheet">
<style>
:root{
  --bg:#8ab83e;
  --bg-light:#a3cc56;
  --bg-dark:#76a532;
  --yellow:#fde26a;
  --ink:#1d1d1d;
  --panel:#ffffff;
  --panel-edge:#e9f2d6;
  --bar:#2c2c2c;
  --green-top:#93c451;
  --green-bot:#5e9a24;
  --col-head:#e2ecc8;
  --col-ink:#4d6a16;
  --row-alt:#efefef;
  --line:#d8d8d8;
  --text:#3a3a3a;
  --link:#555;
}
*{box-sizing:border-box;margin:0;padding:0}
html,body{width:1200px;height:975px;overflow:hidden}
body{font-family:"Open Sans",Arial,sans-serif;background:radial-gradient(ellipse at 50% 20%,var(--bg-light) 0%,var(--bg) 45%,var(--bg-dark) 100%);position:relative;color:var(--text)}
.brand{position:absolute;left:130px;top:26px;font-size:44px;font-weight:700;color:#fff;letter-spacing:-1px;line-height:1}
.top-nav{position:absolute;left:656px;top:0;width:413px;height:26px;background:var(--yellow);border-radius:0 0 8px 8px;display:flex;justify-content:space-around;align-items:center;font-size:14.5px;color:var(--ink)}
.top-nav span+span{border-left:1px solid #b89a22;padding-left:10px}
.main-nav{position:absolute;left:514px;top:44px;width:553px;height:42px;background:#121212;border-radius:6px 14px 8px 16px;display:flex;justify-content:flex-end;align-items:center;gap:0;padding-right:26px}
.main-nav a{color:#fff;font-style:italic;font-size:15.5px;text-decoration:underline;padding:0 11px;border-left:1px solid #777}
.main-nav a:first-child{border-left:none}
.panel{position:absolute;left:136px;top:103px;width:936px;height:808px;background:var(--panel-edge);border-radius:10px}
.panel-inner{position:absolute;left:8px;top:13px;width:918px;height:782px;background:var(--panel);border-radius:6px;overflow:hidden}
.hero{position:absolute;left:3px;top:0;width:914px;height:102px;background:linear-gradient(#8ec04b,#5f9a28)}
.hero-photo{position:absolute;left:17px;top:-10px;width:638px;height:112px;background:linear-gradient(90deg,#b73a2c,#e0c9a8 40%,#c7382c 70%,#7c9d57)}
.social{position:absolute;left:699px;top:23px;width:164px;height:63px;background:#000;border-radius:6px;display:flex;align-items:center;gap:12px;padding-left:16px;color:#fff;font-size:16px;line-height:15px}
.social i{display:block;width:32px;height:32px;background:#3b5a98;border-radius:3px}
.title-bar{position:absolute;left:0;top:102px;width:918px;height:35px;background:var(--bar);color:#fff;display:flex;align-items:center;justify-content:space-between;padding:0 20px 0 18px;font-size:14.5px}
.season{display:flex;align-items:center;gap:9px}
.season b{font-weight:400;background:#4a4a4a;font-size:12px;padding:4px 28px 4px 9px;border-radius:2px;position:relative}
.season b::after{content:"";position:absolute;right:8px;top:10px;border:4px solid transparent;border-top-color:#ddd}
.sidebar{position:absolute;left:4px;top:151px;width:212px;height:511px;background:#f3f3f3}
.side-box{margin:7px 7px 0;background:#fff;border-radius:0 0 8px 8px}
.side-box h3{background:linear-gradient(var(--green-top),var(--green-bot));color:#fff;text-align:center;font-size:14px;font-style:italic;font-weight:800;height:24px;line-height:24px}
.side-box ul{list-style:none;padding:2px 0 8px 10px}
.side-box li{font-style:italic;font-weight:700;font-size:13px;color:#111;height:24.4px;line-height:24.4px}
.side-box li::before{content:"•";margin-right:8px}
.select{position:absolute;top:158px;height:30px;border:1px solid #ccc;border-radius:3px;font-size:12px;padding:0 12px;line-height:28px;color:#444;background:linear-gradient(#fff,#f3f3f3)}
.select::after{content:"";position:absolute;right:12px;top:11px;border:6px solid transparent;border-top-color:#888}
.day{position:absolute;left:229px;width:678px;border:1px solid #c9d6ae;border-radius:6px 6px 3px 3px;overflow:hidden}
.day h2{height:37px;line-height:37px;text-align:center;color:#fff;font-weight:400;font-size:16.5px;background:linear-gradient(var(--green-top),var(--green-bot))}
table{border-collapse:collapse;width:100%;table-layout:fixed;font-size:13px}
th{background:var(--col-head);color:var(--col-ink);font-weight:400;font-size:13.5px;height:34px;text-align:left;padding-left:12px;border-right:1px solid #fff}
td{height:27.5px;border-right:1px solid var(--line);padding-left:10px;white-space:nowrap;overflow:hidden}
tr:nth-child(even) td{background:var(--row-alt)}
td.c{padding:0;text-align:center}
td.vs{padding-left:12px}
.loc{color:var(--link);text-decoration:underline}
.loc.sm,.sm{font-size:11.5px}
.loc.blue{color:#1d3aa8}
.plain{color:var(--link);font-size:11.5px}
.jersey{width:22px;height:20px;vertical-align:middle}
.footer{position:absolute;left:141px;top:932px;color:#fff;font-size:10.5px;letter-spacing:1px}
</style>
</head>
<body>
<svg width="0" height="0" style="position:absolute">
  <symbol id="shirt" viewBox="0 0 24 22"><path d="M7 1 L2 4 L0 9 L4 10 L5 7 L5 21 L19 21 L19 7 L20 10 L24 9 L22 4 L17 1 Q12 5 7 1Z" stroke="#777" stroke-width=".6"/></symbol>
</svg>

<div class="brand">RPL Sports</div>
<nav class="top-nav"><span>Home</span><span>About Us</span><span>FAQS</span><span>Contact Us</span><span>Jobs</span></nav>
<nav class="main-nav"><a>Leagues</a><a>Schedules &amp; More</a><a>Register</a><a>Pay</a><a>Forum</a><a>Sponsors</a></nav>

<div class="panel"><div class="panel-inner">
  <div class="hero">
    <div class="hero-photo" role="img" aria-label="Row of league players in hockey jerseys and helmets"></div>
    <div class="social"><i></i><span>Find Us On<br>Friendnet</span></div>
  </div>
  <div class="title-bar"><span>WEDNESDAY CO-ED BALL HOCKEY SCHEDULE</span><span class="season">Season: <b>Fall 2013</b></span></div>

  <aside class="sidebar">
    <div class="side-box"><h3>Schedules</h3><ul><li>Division A</li><li>Division B</li><li>Division C</li><li>All Divisions</li><li>Playoffs</li></ul></div>
    <div class="side-box"><h3>Stats Menu</h3><ul><li>Game Results</li><li>Scoreboard</li><li>Standings</li><li>Leaders</li></ul></div>
    <div class="side-box"><h3>Quick Links</h3><ul><li>Rules</li><li>Teams</li><li>News</li><li>Free Agents</li><li>Champ T-Shirt Request</li></ul></div>
  </aside>

  <div class="select" style="left:234px;width:252px">- Select team-</div>
  <div class="select" style="left:654px;width:252px">Regular Season/Exhibition</div>

  <section class="day" style="top:199px">
    <h2>Wednesday, Oct 2nd</h2>
    <table>
      <colgroup><col style="width:45px"><col style="width:72px"><col style="width:137px"><col style="width:39px"><col style="width:36px"><col style="width:118px"><col style="width:35px"><col style="width:129px"><col></colgroup>
      <tr><th>TIME</th><th></th><th>HOME</th><th></th><th></th><th>AWAY</th><th></th><th>LOCATION</th><th>STICKS</th></tr>
      <tr><td>Rs.</td><td>08:00 pm</td><td>BOHICA</td><td class="c"><svg class="jersey" fill="#f39a1d"><use href="#shirt"/></svg></td><td class="vs">vs.</td><td>Slap That Pass</td><td class="c"><svg class="jersey" fill="#f7e81c"><use href="#shirt"/></svg></td><td><span class="loc">Horizon Centre</span></td><td></td></tr>
      <tr><td>Rs.</td><td>09:00 pm</td><td>Crown On the Rocks</td><td class="c"><svg class="jersey" fill="#fff"><use href="#shirt"/></svg></td><td class="vs">vs.</td><td>Slap That Pass</td><td class="c"><svg class="jersey" fill="#111"><use href="#shirt"/></svg></td><td><span class="loc">Horizon Centre</span></td><td></td></tr>
    </table>
  </section>

  <section class="day" style="top:344px">
    <h2>Wednesday, Oct 9th</h2>
    <table>
      <colgroup><col style="width:45px"><col style="width:72px"><col style="width:137px"><col style="width:39px"><col style="width:36px"><col style="width:118px"><col style="width:35px"><col style="width:129px"><col></colgroup>
      <tr><th>TIME</th><th></th><th>HOME</th><th></th><th></th><th>AWAY</th><th></th><th>LOCATION</th><th>STICKS</th></tr>
      <tr><td>Rs.</td><td>07:00 pm</td><td>Slap That Pass</td><td class="c"><svg class="jersey" fill="#f7e81c"><use href="#shirt"/></svg></td><td class="vs">vs.</td><td>Faux Tiles</td><td class="c"><svg class="jersey" fill="#b43dd6"><use href="#shirt"/></svg></td><td><span class="loc">Horizon Centre</span></td><td></td></tr>
      <tr><td>Rs.</td><td>08:45 pm</td><td>Hamburglars</td><td class="c"><svg class="jersey" fill="#111"><use href="#shirt"/></svg></td><td class="vs">vs.</td><td>Those Guys</td><td class="c"><svg class="jersey" fill="#fff"><use href="#shirt"/></svg></td><td><span class="plain">Eastbrook (EBK)</span></td><td></td></tr>
      <tr><td>Rs.</td><td>09:45 pm</td><td>Crown On The Rocks</td><td class="c"><svg class="jersey" fill="#ddd"><use href="#shirt"/></svg></td><td class="vs">vs.</td><td>BOHICA</td><td class="c"><svg class="jersey" fill="#f39a1d"><use href="#shirt"/></svg></td><td><span class="plain">Eastbrook (EBK)</span></td><td></td></tr>
    </table>
  </section>

  <section class="day" style="top:521px;left:231px">
    <h2>Wednesday, Oct 16th</h2>
    <table>
      <colgroup><col style="width:45px"><col style="width:72px"><col style="width:137px"><col style="width:39px"><col style="width:36px"><col style="width:118px"><col style="width:35px"><col style="width:129px"><col></colgroup>
      <tr><th>TIME</th><th></th><th>HOME</th><th></th><th></th><th>AWAY</th><th></th><th>LOCATION</th><th>STICKS</th></tr>
      <tr><td>Rs.</td><td>08:00 pm</td><td>Ball Handlers</td><td class="c"><svg class="jersey" fill="#e8141c"><use href="#shirt"/></svg></td><td class="vs">vs.</td><td>BOHICA</td><td class="c"><svg class="jersey" fill="#f39a1d"><use href="#shirt"/></svg></td><td><span class="loc">Horizon Centre</span></td><td></td></tr>
      <tr><td>Rs.</td><td>09:00 pm</td><td>Shooting Seamen</td><td class="c"><svg class="jersey" fill="#3a2ad8"><use href="#shirt"/></svg></td><td class="vs">vs.</td><td class="sm">Crown On The Rocks</td><td class="c"><svg class="jersey" fill="#fff"><use href="#shirt"/></svg></td><td><span class="loc">Horizon Centre</span></td><td></td></tr>
      <tr><td>Rs.</td><td>08:30 pm</td><td>Dirty Danglers</td><td class="c"><svg class="jersey" fill="#111"><use href="#shirt"/></svg></td><td class="vs">vs.</td><td>Slap That Pass</td><td class="c"><svg class="jersey" fill="#f7e81c"><use href="#shirt"/></svg></td><td><span class="loc blue">N.R.P.C.A</span></td><td></td></tr>
      <tr><td>Rs.</td><td>08:30 pm</td><td>Chiefs</td><td class="c"><svg class="jersey" fill="#3a2ad8"><use href="#shirt"/></svg></td><td class="vs">vs.</td><td>Hamburglars</td><td class="c"><svg class="jersey" fill="#111"><use href="#shirt"/></svg></td><td><span class="plain">Eastbrook (EBK)</span></td><td></td></tr>
    </table>
  </section>
</div></div>

<footer class="footer">© 2011, RPL SPORTS. ALL RIGHTS RESERVED.</footer>
</body>
</html>
```